Pelican Drift - Caffeine Supplement for everyday use & pre-workout

Online marketplace focussing on caffeine supplements for everyday use and pre-workouts. Selling point is this product is not as strong as the existing pre-workouts to avoid crashing and uncomfortable levels of energy. Ideal for endurance sports athletes as an inter-workout supplement to maintain energy levels. Initially 4 categories, stand-alone tubs, stacks (2/3 tubs), taster packs and merchandise (shaker bottles) etc.

Target Market(s)

under 40s across the fitness imdustry

Industry/Entity Type

Supplement

Coding

Coded - Design and coding required

Font styles to use
Sans Serif

Colors
ec1f27
ffffff

Requirements
Must have
• Home Page
About Page
Product Page
Contact Page
Basket
Woocommerce capability
Nice to have
• Fixed Header so when scrolling it remains fixed on page.

Logo on left hand side. 4 links on the right hand side (Home, Products, About, Basket)

```html
<!DOCTYPE html>
<html lang="en">
<head>
<meta charset="utf-8">
<title>Pelican Drift – Caffeine Supplement</title>
<link rel="stylesheet" href="https://fonts.googleapis.com/css2?family=Raleway:wght@400;500;600;700;800&family=Questrial&display=swap">
<style>
:root{
  --red:#ec1f27;
  --red-dark:#b8101a;
  --white:#ffffff;
  --ink:#111111;
  --night:#0c0c0e;
  --grey-text:#6b6b6b;
  --line:#dddddd;
  --faint:#f1f1f1;
  --skin:#d8c2ae;
  --slate:#3b464e;
}
*{margin:0;padding:0;box-sizing:border-box}
html,body{width:1200px;height:4248px;overflow:hidden}
body{position:relative;background:var(--white);font-family:"Questrial",sans-serif;color:var(--ink)}
.abs{position:absolute}
.heading{font-family:"Raleway",sans-serif;font-weight:600;font-size:33px;letter-spacing:.5px;text-transform:uppercase;white-space:nowrap}
.heading .accent{color:var(--red)}
.rule{position:absolute;height:3px;background:var(--red)}
.btn{position:absolute;display:flex;align-items:center;justify-content:center;background:var(--red);color:var(--white);font-family:"Raleway",sans-serif;font-weight:700;font-size:16px;border-radius:30px;text-transform:uppercase}
.brand{display:flex;align-items:center;gap:10px;font-family:"Raleway",sans-serif;font-weight:800;color:var(--white);white-space:nowrap}
.brand .dot{width:22px;height:22px;border-radius:50%;background:var(--red)}

/* hero */
.hero{left:0;top:0;width:1200px;height:602px;background:linear-gradient(100deg,#5b4a3d 0%,#3a2f28 35%,#2b2522 60%,#3b332e 100%)}
.hero-shade{left:0;top:0;width:1200px;height:602px;background:linear-gradient(90deg,rgba(0,0,0,0) 30%,rgba(0,0,0,.45) 60%)}
.nav-brand{left:109px;top:38px;font-size:32px}
.nav{left:0;top:46px;font-family:"Raleway",sans-serif;font-weight:700;font-size:13.5px;color:var(--white)}
.nav a{position:absolute;white-space:nowrap;text-decoration:none;color:inherit}
.nav a.active{color:var(--red)}
.login{left:964px;top:33px;width:127px;height:43px;font-size:16px}
.side-word{font-family:"Raleway",sans-serif;font-weight:700;font-size:12px;color:var(--white);width:14px;text-align:center;line-height:32px}
.hero-bar{left:531px;top:186px;width:4px;height:194px;background:var(--red)}
.hero-title{left:549px;top:180px;font-family:"Raleway",sans-serif;font-weight:800;font-size:52px;line-height:58px;color:var(--white);text-transform:uppercase;white-space:nowrap}
.hero-title .accent{color:var(--red)}
.hero-copy{left:549px;top:312px;width:540px;font-size:14px;line-height:28px;color:var(--white)}
.get-started{left:549px;top:382px;width:179px;height:56px}

/* about */
.about-mark{left:170px;top:700px;width:860px;text-align:center;font-family:"Raleway",sans-serif;font-weight:800;font-size:170px;line-height:1;color:var(--faint);letter-spacing:-2px}
.about-mark-sub{left:170px;top:985px;width:860px;text-align:center;font-family:"Raleway",sans-serif;font-weight:700;font-size:64px;letter-spacing:58px;color:#fbeaea}
.about-title{left:0;top:708px;width:1200px;text-align:center}
.about-rule{left:566px;top:758px;width:68px}
.about-copy{left:150px;top:805px;width:900px;text-align:center;font-size:14.5px;line-height:30px;color:var(--grey-text)}
.learn-more{left:494px;top:952px;width:183px;height:57px}

/* products */
.products{left:0;top:1108px;width:1200px;height:812px}
.products-photo{left:0;top:1150px;width:1200px;height:740px;background:radial-gradient(ellipse at 18% 45%,rgba(255,120,120,.35),rgba(0,0,0,0) 45%),radial-gradient(ellipse at 88% 25%,rgba(255,150,150,.25),rgba(0,0,0,0) 30%)}
.products-title{left:0;top:1240px;width:1200px;text-align:center;color:var(--white)}
.tabs{left:0;top:1334px;width:1200px;font-family:"Raleway",sans-serif;font-weight:500;font-size:14px;color:#111}
.tabs span{position:absolute;white-space:nowrap;transform:translateX(-50%)}
.tabs span.current{color:var(--white)}
.card{position:absolute;top:1383px;width:231px;height:260px;background:var(--white)}
.tub{position:absolute;left:66px;top:30px;width:100px;height:205px;border-radius:18px 18px 14px 14px}
.tub-cap{position:absolute;left:82px;top:28px;width:68px;height:30px;border-radius:6px}
.card-label{position:absolute;top:1664px;width:231px;text-align:center;font-size:14px;color:var(--white)}
.stars{position:absolute;top:1695px;width:231px;text-align:center;color:var(--white);font-size:14px;letter-spacing:3px}

/* benefits */
.benefits-photo{left:600px;top:1912px;width:600px;height:827px;background:linear-gradient(90deg,rgba(255,255,255,1) 0%,rgba(216,194,174,.55) 40%,var(--skin) 70%,#b9a593 100%)}
.benefits-photo-low{left:600px;top:2330px;width:600px;height:409px;background:linear-gradient(90deg,rgba(59,70,78,0) 0%,rgba(59,70,78,.6) 40%,var(--slate) 75%)}
.benefits-title{left:110px;top:1985px}
.benefits-rule{left:110px;top:2045px;width:122px}
.diamond{position:absolute;width:214px;height:214px;border:1px solid #cfcfcf;transform:rotate(45deg);background:var(--white)}
.hub{left:401px;top:2247px;width:154px;height:154px;border-radius:50%;background:var(--red);display:flex;align-items:center;justify-content:center;color:var(--white);font-family:"Raleway",sans-serif;font-weight:800;font-size:21px;text-align:center;line-height:1.05}
.icon{position:absolute;width:80px;height:80px;border-radius:50%;background:var(--red);display:flex;align-items:center;justify-content:center}
.benefit-label{position:absolute;width:190px;text-align:center;font-family:"Raleway",sans-serif;font-weight:600;font-size:15.5px;line-height:30px;letter-spacing:.6px;text-transform:uppercase;color:#222}

/* offers */
.offers{left:0;top:2739px;width:1200px;height:565px;background:var(--night)}
.offers-photo{left:20px;top:2760px;width:480px;height:490px;background:radial-gradient(ellipse at 40% 55%,#3a3d4a 0%,#1d1f27 45%,rgba(12,12,14,0) 75%)}
.offers-title{left:597px;top:2870px;color:var(--white)}
.offers-rule{left:597px;top:2932px;width:122px}
.offers-copy{left:600px;top:2962px;width:490px;font-size:14.5px;line-height:30px;color:var(--white)}
.shop-now{left:600px;top:3141px;width:181px;height:56px}

/* testimonials */
.testi-title{left:0;top:3391px;width:1200px;text-align:center}
.testi-rule{left:566px;top:3453px;width:68px}
.testi-card{position:absolute;top:3482px;width:356px;height:241px;border:1px solid var(--line);background:var(--white)}
.quote{position:absolute;left:22px;top:14px;font-family:"Raleway",sans-serif;font-weight:800;font-size:26px;color:var(--red)}
.testi-copy{position:absolute;left:22px;top:40px;width:298px;font-size:14px;line-height:30px;color:var(--grey-text)}
.avatar{position:absolute;left:22px;top:165px;width:56px;height:56px;border-radius:50%;background:linear-gradient(160deg,#c9c9c9,#6d6d6d)}
.testi-name{position:absolute;left:96px;top:183px;font-size:16px;color:var(--red)}

/* footer */
.footer{left:0;top:3780px;width:1200px;height:468px}
.foot-brand{left:96px;top:3938px;font-size:30px}
.foot-copy{left:93px;top:4010px;width:270px;font-size:15px;line-height:26px;color:var(--white)}
.foot-head{position:absolute;top:3936px;font-family:"Raleway",sans-serif;font-weight:700;font-size:15px;color:var(--white);text-transform:uppercase;white-space:nowrap}
.foot-head .accent{color:var(--red)}
.foot-list{position:absolute;top:3976px;list-style:none;font-size:15px;line-height:25.7px;color:var(--white);white-space:nowrap}
.foot-list li::before{content:"»";margin-right:18px}
.contact-row{position:absolute;left:892px;display:flex;gap:16px;font-size:15px;line-height:25px;color:var(--white);white-space:nowrap}
.contact-row svg{flex:none;margin-top:5px}
.foot-divider{left:80px;top:4161px;width:1040px;height:1px;background:#333}
.copyright{left:0;top:4182px;width:1200px;text-align:center;font-family:"Raleway",sans-serif;font-weight:600;font-size:13px;color:var(--white)}
.copyright .accent{color:var(--red)}
</style>
</head>
<body>

<!-- HERO -->
<div class="abs hero" role="img" aria-label="Woman drinking from a shaker bottle in a gym"></div>
<div class="abs hero-shade"></div>
<svg class="abs" style="left:0;top:540px" width="1200" height="62" viewBox="0 0 1200 62" aria-hidden="true">
  <polygon points="0,20 1200,58 1200,62 0,62" fill="#ffffff"/>
  <polygon points="0,20 560,38 0,60" fill="var(--red)"/>
</svg>
<div class="abs brand nav-brand"><span class="dot"></span>Pelican Drift</div>
<nav class="abs nav">
  <a class="active" style="left:364px">HOME</a>
  <a style="left:460px">ABOUT US</a>
  <a style="left:581px">PRODUCTS</a>
  <a style="left:707px">BASKET</a>
  <a style="left:810px">CONTACT US</a>
</nav>
<div class="btn login">
  <svg width="14" height="15" viewBox="0 0 14 15" style="margin-right:6px" aria-hidden="true"><circle cx="7" cy="4" r="3.6" fill="#fff"/><path d="M0 15c0-4.5 3-7 7-7s7 2.5 7 7z" fill="#fff"/></svg>Login
</div>
<div class="abs side-word" style="left:30px;top:252px">P<br>R<br>E<br>V</div>
<div class="abs side-word" style="left:1131px;top:252px">N<br>E<br>X<br>T</div>
<div class="abs hero-bar"></div>
<h1 class="abs hero-title">Begin <span class="accent">your fitness</span><br>journey</h1>
<p class="abs hero-copy">Lorem ipsum dolor sit amet, consectetur adipiscing elit, sed do eiusmod tempor incididunt ut labore et dolore magna aliqua.</p>
<div class="btn get-started">Get Started</div>

<!-- ABOUT -->
<div class="abs about-mark" aria-hidden="true">Pelican</div>
<div class="abs about-mark-sub" aria-hidden="true">DRIFT</div>
<h2 class="abs heading about-title">About <span class="accent">Pelican Drift</span></h2>
<div class="rule about-rule"></div>
<p class="abs about-copy">Lorem ipsum dolor sit amet, consectetur adipiscing elit, sed do eiusmod tempor incididunt ut labore et dolore magna aliqua. Ut enim ad minim veniam, quis nostrud exercitation ullamco laboris nisi ut aliquip ex ea commodo consequat. Duis aute irure dolor in reprehenderit in voluptate velit esse cillum dolore eu fugiat nulla pariatur. Excepteur sint occaecat cupidatat non proident, sunt in culpa qui officia deserunt mollit anim id est laborum.</p>
<div class="btn learn-more">Learn More</div>

<!-- PRODUCTS -->
<svg class="abs products" width="1200" height="812" viewBox="0 0 1200 812" aria-hidden="true">
  <polygon points="0,47 1200,0 1200,47" fill="#0a0a0a"/>
  <polygon points="0,47 1200,47 1200,812 0,775" fill="var(--red)"/>
  <polygon points="0,729 1200,775 1200,812 0,775" fill="#0a0a0a"/>
  <polygon points="0,775 1200,812 0,812" fill="#ffffff"/>
</svg>
<div class="abs products-photo" role="img" aria-label="Athlete and shaker bottle tinted red behind the product grid"></div>
<h2 class="abs heading products-title">Pelican Drift Products</h2>
<div class="abs tabs">
  <span style="left:295px">All</span><span style="left:337px">|</span>
  <span class="current" style="left:434px">Stand-alone Tubs</span><span style="left:528px">|</span>
  <span style="left:583px">Stacks</span><span style="left:639px">|</span>
  <span style="left:715px">Taster Packs</span><span style="left:792px">|</span>
  <span style="left:872px">Merchandise</span>
</div>
<div class="card" style="left:112px" role="img" aria-label="Black supplement tub"><div class="tub" style="background:linear-gradient(90deg,#111,#3a3a3a 45%,#111)"></div><div class="tub-cap" style="background:#222"></div></div>
<div class="card" style="left:359px" role="img" aria-label="White supplement tub"><div class="tub" style="background:linear-gradient(90deg,#cfcfcf,#ffffff 45%,#bdbdbd)"></div><div class="tub-cap" style="background:#e2e2e2"></div></div>
<div class="card" style="left:608px" role="img" aria-label="Red supplement tub"><div class="tub" style="background:linear-gradient(90deg,#a30d14,#f04048 45%,#a30d14)"></div><div class="tub-cap" style="background:#c8141c"></div></div>
<div class="card" style="left:855px" role="img" aria-label="Green supplement tub"><div class="tub" style="background:linear-gradient(90deg,#2f6b1d,#5fa63c 45%,#2f6b1d)"></div><div class="tub-cap" style="background:#44852a"></div></div>
<div class="card-label" style="left:112px">Stand-alone Tubs</div>
<div class="card-label" style="left:359px">Stand-alone Tubs</div>
<div class="card-label" style="left:608px">Stand-alone Tubs</div>
<div class="card-label" style="left:855px">Stand-alone Tubs</div>
<div class="stars" style="left:112px">★★★★★</div>
<div class="stars" style="left:359px">★★★★★</div>
<div class="stars" style="left:608px">★★★★★</div>
<div class="stars" style="left:855px">★★★★★</div>

<!-- BENEFITS -->
<div class="abs benefits-photo" role="img" aria-label="Photograph of a smiling athletic woman in a sports top"></div>
<div class="abs benefits-photo-low" aria-hidden="true"></div>
<h2 class="abs heading benefits-title">Our <span class="accent">Benefits</span></h2>
<div class="rule benefits-rule"></div>
<div class="diamond" style="left:387px;top:2035px"></div>
<div class="diamond" style="left:206px;top:2200px"></div>
<div class="diamond" style="left:552px;top:2200px"></div>
<div class="diamond" style="left:363px;top:2382px"></div>
<div class="abs hub">Pelican<br>Drift</div>
<div class="icon" style="left:453px;top:2068px"><svg width="40" height="40" viewBox="0 0 40 40" fill="none" stroke="#000" stroke-width="2.2" aria-hidden="true"><circle cx="20" cy="20" r="12"/><path d="M14 20h12M20 14v12"/></svg></div>
<div class="icon" style="left:280px;top:2211px"><svg width="40" height="40" viewBox="0 0 40 40" fill="none" stroke="#000" stroke-width="2.2" aria-hidden="true"><circle cx="20" cy="9" r="4"/><path d="M8 16h24M20 14v12M14 36l6-10 6 10"/></svg></div>
<div class="icon" style="left:614px;top:2214px"><svg width="40" height="40" viewBox="0 0 40 40" fill="none" stroke="#000" stroke-width="2.2" aria-hidden="true"><rect x="7" y="12" width="6" height="16"/><rect x="27" y="12" width="6" height="16"/><path d="M3 20h4M13 20h14M33 20h4"/></svg></div>
<div class="icon" style="left:428px;top:2411px"><svg width="40" height="40" viewBox="0 0 40 40" fill="none" stroke="#000" stroke-width="2.2" aria-hidden="true"><path d="M10 10h20M14 10v20h12V10M12 30h16"/></svg></div>
<div class="benefit-label" style="left:399px;top:2160px">Regulates eating habits</div>
<div class="benefit-label" style="left:215px;top:2305px">Improves bone density</div>
<div class="benefit-label" style="left:560px;top:2314px">Enhances quality of life</div>
<div class="benefit-label" style="left:375px;top:2505px">Increases physical capacity</div>

<!-- OFFERS -->
<div class="abs offers"></div>
<div class="abs offers-photo" role="img" aria-label="Supplement tubs, shaker bottle, scoop of powder and tablets"></div>
<svg class="abs" style="left:0;top:3250px" width="1200" height="54" viewBox="0 0 1200 54" aria-hidden="true">
  <polygon points="0,10 1200,54 0,54" fill="var(--red)"/>
  <polygon points="0,40 1200,54 0,54" fill="var(--red-dark)"/>
</svg>
<h2 class="abs heading offers-title">Our best <span class="accent">offers</span></h2>
<div class="rule offers-rule"></div>
<p class="abs offers-copy">Lorem ipsum dolor sit amet, consectetur adipiscing elit, sed do eiusmod tempor incididunt ut labore et dolore magna aliqua. Ut enim ad minim veniam, quis nostrud exercitation ullamco laboris nisi ut aliquip ex ea commodo consequat. Duis aute irure dolor in reprehenderit in voluptate velit esse cillum.</p>
<div class="btn shop-now">Shop Now</div>

<!-- TESTIMONIALS -->
<h2 class="abs heading testi-title">Our client <span class="accent">testimonials</span></h2>
<div class="rule testi-rule"></div>
<div class="testi-card" style="left:54px"><span class="quote">“</span><p class="testi-copy">Sed ut perspiciatis unde omnis iste natus error sit voluptatem accusantium dolor emque laudantium, totam rem aperiam, eaque ipsa quae ab illo inventore .</p><div class="avatar" role="img" aria-label="Customer portrait"></div><span class="testi-name">John Deo</span></div>
<div class="testi-card" style="left:422px"><span class="quote">“</span><p class="testi-copy">Sed ut perspiciatis unde omnis iste natus error sit voluptatem accusantium dolor emque laudantium, totam rem aperiam, eaque ipsa quae ab illo inventore .</p><div class="avatar" role="img" aria-label="Customer portrait"></div><span class="testi-name">John Deo</span></div>
<div class="testi-card" style="left:789px"><span class="quote">“</span><p class="testi-copy">Sed ut perspiciatis unde omnis iste natus error sit voluptatem accusantium dolor emque laudantium, totam rem aperiam, eaque ipsa quae ab illo inventore .</p><div class="avatar" role="img" aria-label="Customer portrait"></div><span class="testi-name">John Deo</span></div>

<!-- FOOTER -->
<svg class="abs footer" width="1200" height="468" viewBox="0 0 1200 468" aria-hidden="true">
  <polygon points="0,20 1200,85 1200,468 0,468" fill="#0a0a0a"/>
  <polygon points="420,40 1200,55 1200,88 0,60" fill="var(--red)"/>
  <polygon points="0,60 1200,88 1200,100 0,75" fill="#0a0a0a"/>
</svg>
<div class="abs brand foot-brand"><span class="dot"></span>Pelican Drift</div>
<p class="abs foot-copy">Lorem ipsum dolor sit amet, consectetur adipiscing elit, sed do eiusmod tempor incididunt ut labore et dolore magna aliqua.</p>
<div class="foot-head" style="left:447px"><span class="accent">Quick</span> Links</div>
<ul class="foot-list" style="left:447px"><li>Home</li><li>About Us</li><li>Products</li><li>Basket</li><li>Contact Us</li></ul>
<div class="foot-head" style="left:661px"><span class="accent">Our</span> Products</div>
<ul class="foot-list" style="left:661px"><li>Stand-alone tubs</li><li>Stacks</li><li>Taster packs</li><li>Merchandise</li></ul>
<div class="foot-head" style="left:892px"><span class="accent">Contact</span> Info</div>
<div class="contact-row" style="top:3975px"><svg width="12" height="16" viewBox="0 0 12 16" aria-hidden="true"><path d="M6 0a6 6 0 0 1 6 6c0 4.5-6 10-6 10S0 10.5 0 6a6 6 0 0 1 6-6z" fill="var(--red)"/><circle cx="6" cy="6" r="2.2" fill="#0a0a0a"/></svg><span>Lorem ipsum dolor sit<br>amet, consectetur</span></div>
<div class="contact-row" style="top:4040px"><svg width="14" height="14" viewBox="0 0 14 14" aria-hidden="true"><path d="M3 0l3 3-2 2c1 2 3 4 5 5l2-2 3 3-2 3C6 14 0 8 0 3z" fill="var(--red)"/></svg><span>1 888 888 8888</span></div>
<div class="contact-row" style="top:4080px"><svg width="15" height="11" viewBox="0 0 15 11" aria-hidden="true"><rect width="15" height="11" rx="1" fill="var(--red)"/><path d="M0 1l7.5 5L15 1" stroke="#0a0a0a" stroke-width="1.3" fill="none"/></svg><span>info@pelicandrift.com</span></div>
<div class="abs foot-divider"></div>
<p class="abs copyright">© Copyrights 2020 <span class="accent">Pelican Drift</span> &nbsp;&nbsp;|&nbsp;&nbsp; All Rights Reserved</p>

</body>
</html>
```